Flyer Design

I recently got a website designed by Pagecraft - www.tidynestliving.com.au

I own an organisational business. We help people to simplify their homes which in turn, creates a more balanced and healthy life. We offer de-clutter services for pantries, wardrobes, linen cupboards, home offices, and anywhere you need a bit of organisation. We can help you with de-cluttering and property styling that will help to sell your home. In addition, we provide help with moving, packing and unpacking, or even downsizing. With our keen eye for detail and passion for interior design, we will not only provide a practical solution, but a wonderful design element to your home. Tidy Nest Living is a proud member of the Southern Guild of Certified Space Planners Inc.

Can I please use the logo off my website. I have also put it below.

Industry/Entity Type

Business

```html
<!DOCTYPE html>
<html lang="en">
<head>
<meta charset="utf-8">
<title>Tidy Nest Living – Flyer</title>
<link rel="stylesheet" href="https://fonts.googleapis.com/css2?family=Lato:wght@400;700;900&family=Archivo+Narrow:wght@700&display=swap">
<style>
  :root {
    --backdrop: #0e1113;
    --mint: #64ecd0;
    --mint-soft: #8ff5de;
    --ink: #111111;
    --white: #ffffff;
    --band-light: rgba(255,255,255,0.55);
    --band-dark: rgba(40,48,50,0.72);
  }
  * { margin: 0; padding: 0; box-sizing: border-box; }
  html, body { width: 1200px; height: 912px; overflow: hidden; background: var(--backdrop); }
  .canvas { position: relative; width: 1200px; height: 912px; }
  .flyer {
    position: absolute; left: 120px; top: 116px; width: 960px; height: 680px;
    background: var(--white); overflow: hidden;
    font-family: "Lato", sans-serif;
  }
  .hero { position: absolute; left: 0; top: 0; width: 960px; height: 379px; }
  .hero svg { display: block; }
  .tagline {
    position: absolute; font-family: "Archivo Narrow", sans-serif; font-weight: 700;
    font-size: 21px; line-height: 1.2; display: flex; align-items: center;
  }
  .tagline--unclutter { left: 0; top: 202px; width: 352px; height: 48px; background: var(--band-light); color: var(--ink); padding-left: 26px; }
  .tagline--passion { left: 335px; top: 289px; width: 290px; height: 47px; background: var(--band-dark); color: var(--white); padding-left: 10px; }
  .tagline--storage { left: 640px; top: 265px; width: 320px; height: 72px; background: var(--band-dark); color: var(--white); justify-content: center; text-align: center; }
  .about {
    position: absolute; left: 0; top: 379px; width: 960px; height: 168px;
    background: var(--mint); color: var(--white); padding: 12px 36px 0 36px;
    border-top: 3px solid var(--white);
  }
  .about__title { font-size: 21px; font-weight: 700; margin-bottom: 3px; }
  .about__body { font-size: 15.6px; line-height: 19.5px; }
  .footer { position: absolute; left: 0; top: 547px; width: 960px; height: 133px; }
  .brand {
    position: absolute; left: 40px; top: 62px; display: flex; align-items: center; gap: 12px;
    font-family: "Lato", sans-serif; font-weight: 900; font-size: 30px; color: var(--ink);
  }
  .brand__mark { width: 34px; height: 34px; background: var(--mint-soft); }
  .contact { position: absolute; left: 542px; top: 38px; font-size: 18px; line-height: 24.5px; color: var(--ink); }
  .contact dt { display: inline; font-weight: 900; }
  .contact dd { display: inline; margin-left: 4px; }
  .contact div { white-space: nowrap; }
</style>
</head>
<body>
<div class="canvas">
  <article class="flyer">
    <section class="hero">
      <svg width="960" height="379" viewBox="0 0 960 379">
        <defs>
          <linearGradient id="kitchen" x1="0" y1="0" x2="0" y2="1">
            <stop offset="0" stop-color="#d9f3ec"/>
            <stop offset="0.6" stop-color="#b9d6cf"/>
            <stop offset="1" stop-color="#6d8580"/>
          </linearGradient>
          <linearGradient id="bedroom" x1="0" y1="0" x2="0" y2="1">
            <stop offset="0" stop-color="#c8eee4"/>
            <stop offset="0.45" stop-color="#6d7f7c"/>
            <stop offset="0.7" stop-color="#e6f2ef"/>
            <stop offset="1" stop-color="#5d6c6a"/>
          </linearGradient>
          <linearGradient id="wardrobe" x1="0" y1="0" x2="1" y2="1">
            <stop offset="0" stop-color="#c9ece0"/>
            <stop offset="0.4" stop-color="#7f7a8c"/>
            <stop offset="0.75" stop-color="#4e5b7a"/>
            <stop offset="1" stop-color="#c0506e"/>
          </linearGradient>
        </defs>
        <rect width="960" height="379" fill="url(#kitchen)" role="img" aria-label="Photo of a tidy kitchen bench with sink and kettle"/>
        <path d="M300 0 H610 Q720 190 620 379 H330 Q370 190 300 0 Z" fill="url(#bedroom)" stroke="#ffffff" stroke-width="4" role="img" aria-label="Photo of a neatly made bed with a patterned cushion"/>
        <path d="M0 0 H300 Q370 190 330 379 H0 Z" fill="url(#wardrobe)" stroke="#ffffff" stroke-width="4" role="img" aria-label="Photo of shirts hanging on wooden hangers in a wardrobe"/>
      </svg>
      <div class="tagline tagline--unclutter">Unclutter Your Life Today</div>
      <div class="tagline tagline--passion">Organising Is Our Passion</div>
      <div class="tagline tagline--storage">Storage Solutions<br>Customized For You</div>
    </section>

    <section class="about">
      <h2 class="about__title">Uncluttering Life – One Home at a Time</h2>
      <p class="about__body">&nbsp;&nbsp;At Tidy Nest Living, it is our goal to unclutter life, one house at a time. Whether you are planning a move and need to downsize, or you just need some basic organisation and storage, we are here for you, every step of the way. We help people to simplify their homes which in turn, creates a more balanced and healthy life. We put into place basic organisation systems that work for you and your family. We customise solutions to your unique needs, ensuring that your home offers practical yet attractive storage.<br>When you are ready to live life de-cluttered, we are ready to help. Phone us today to schedule a consultation!</p>
    </section>

    <footer class="footer">
      <div class="brand"><span class="brand__mark"></span><span class="brand__name">Tidy Nest Living</span></div>
      <dl class="contact">
        <div><dt>Phone :</dt><dd>0400 123 456</dd></div>
        <div><dt>Email :</dt><dd>hello@tidynestliving.com.au</dd></div>
        <div><dt>Website :</dt><dd>www.tidynestliving.com.au</dd></div>
      </dl>
    </footer>
  </article>
</div>
</body>
</html>
```